Modern Banner and Window Decal Design For Law Firm Lawyer

We are looking for three modern and sophisticated banner design and window decal for our law firm.

Banner measurements/types:

1) Height: 130 cm Width: 160 cm (Outdoor banner)
2) Height: 200 cm Width: 85 cm (Pull up/retractable indoor banner)

Window Decal:
3) Height: 70cm width 70cm

Our law firm is based in Melbourne, Australia and we deal with property law mostly.

We prefer a white background with classic text in black or grey. We would also like a dash of colour so please use a green, blue or aqua colour palette that is consistent with our logo. Vector attached. A nice photo of property, Melbourne city viee, or family home would be nice.

We do not want any law related images - scales of justice, gavel or the like.

Our ultimate goal is to communicate that the firm is modern, professional and knowledgeable

We would like the following:

1. Our logo
2. Our services: - Property Law - Wills - Powers of Attorney - Probate - Estate Administration - Consultancy & Agency
3. Phone number
4. Web Address

5. For pull up/retractable banner we would also like the following text:

We use the latest digital technology and fixed-fees to provide fast and affordable legal advice that is easy to understand.

For privacy reasons, we will provide business details once we have decided on the winner.

We will monitor entries closely and promise to provide feedback and guidance on each entry.

Thank you very much for considering this project.

Target Market(s)

General public, professionals, lawyers and conveyancers

Industry/Entity Type

Law Firm

Font styles to use
Sans Serif

Colors
0393ce
34a6d7
0456a4
3176b5
acd037
33b8a4
86cfc6
00a990
9ccb3b

Requirements
Must have
• 1. Our logo
• 2. Our services: - Property Law - Wills - Powers of Attorney - Probate & Estate Administration - Consultancy & Agency
• 3. Phone number
• 4. Web Address
Nice to have
• Picture of Melbourne, Australia city ; property/buildings/lawyers
Should not have
• We do not want any law related images - scales of justice, gavel or the like.

```html
<!DOCTYPE html>
<html lang="en">
<head>
<meta charset="utf-8">
<title>Ridgeview Lawyers – Pull-up Banner</title>
<link rel="stylesheet" href="https://fonts.googleapis.com/css2?family=Roboto:wght@400;500;700&family=Roboto+Condensed:wght@500;700&display=swap">
<style>
  :root {
    --page-bg: #e9eaec;
    --banner-bg: #ffffff;
    --brand-blue: #1f6fc6;
    --brand-blue-deep: #0456a4;
    --brand-aqua: #34a6d7;
    --heading-light: #8fd3f0;
    --text-dark: #111111;
    --logo-grey: #4a4a4a;
    --photo-sky: #8fb6d6;
    --photo-city: #6c7f8e;
    --photo-water: #1f2d3a;
  }
  * { margin: 0; padding: 0; box-sizing: border-box; }
  html, body { width: 1200px; height: 1000px; overflow: hidden; }
  body { background: var(--page-bg); font-family: "Roboto", Arial, sans-serif; }

  .banner {
    position: absolute; left: 409px; top: 29px;
    width: 382px; height: 942px;
    background: var(--banner-bg);
    overflow: hidden;
    box-shadow: 0 4px 14px rgba(0,0,0,0.18);
  }
  .banner__shapes { position: absolute; inset: 0; }

  .brand {
    position: absolute; left: 40px; top: 58px;
    display: flex; align-items: center; gap: 18px;
  }
  .brand__dot { width: 72px; height: 72px; border-radius: 50%; background: var(--brand-aqua); }
  .brand__name {
    font-family: "Roboto", Arial, sans-serif; font-weight: 400;
    color: var(--logo-grey); font-size: 27px; line-height: 1.15; letter-spacing: 1px;
  }

  .services {
    position: absolute; left: 20px; top: 218px; width: 240px;
    font-family: "Roboto Condensed", Arial, sans-serif; color: #fff;
  }
  .services__title {
    text-align: center; font-weight: 700; font-size: 18px; letter-spacing: 1px;
    line-height: 21px; color: var(--heading-light); margin-bottom: 14px; padding-left: 14px;
  }
  .services__list { list-style: none; }
  .services__item {
    position: relative; padding-left: 18px;
    font-size: 21px; font-weight: 500; line-height: 24px;
    text-transform: uppercase; margin-bottom: 7px; white-space: nowrap;
  }
  .services__item::before {
    content: ""; position: absolute; left: 0; top: 6px;
    width: 11px; height: 11px; background: var(--heading-light);
  }

  .tagline {
    position: absolute; left: 0; top: 794px; width: 100%;
    text-align: center; font-size: 12.5px; font-weight: 700;
    color: var(--text-dark); line-height: 1.3;
  }
  .phone {
    position: absolute; left: 0; top: 838px; width: 100%;
    display: flex; justify-content: center; align-items: center; gap: 10px;
    font-family: "Roboto Condensed", Arial, sans-serif;
    font-size: 33px; font-weight: 700; color: var(--text-dark);
  }
  .phone__icon {
    width: 28px; height: 28px; border-radius: 6px; background: var(--brand-blue);
    display: flex; align-items: center; justify-content: center;
  }
  .web {
    position: absolute; left: 77px; top: 884px; width: 228px; height: 29px;
    border-radius: 6px; background: var(--brand-blue-deep);
    color: #fff; font-size: 16px; text-align: center; line-height: 29px;
  }
</style>
</head>
<body>
  <main class="banner">
    <svg class="banner__shapes" width="382" height="942" viewBox="0 0 382 942">
      <defs>
        <linearGradient id="cityPhoto" x1="0" y1="0" x2="0" y2="1">
          <stop offset="0" stop-color="#8fb6d6"/>
          <stop offset="0.5" stop-color="#6c7f8e"/>
          <stop offset="0.72" stop-color="#4f5a52"/>
          <stop offset="1" stop-color="#1f2d3a"/>
        </linearGradient>
      </defs>
      <circle class="photo-circle" cx="247" cy="553" r="218" fill="url(#cityPhoto)"
              role="img" aria-label="Aerial photo of the Melbourne city skyline beside the river and bridge"/>
      <circle class="services-circle" cx="130" cy="320" r="150" fill="#1f6fc6" fill-opacity="0.9"/>
    </svg>

    <header class="brand">
      <span class="brand__dot"></span>
      <span class="brand__name">RIDGEVIEW<br>LAWYERS</span>
    </header>

    <section class="services">
      <h2 class="services__title">OUR SERVICES:</h2>
      <ul class="services__list">
        <li class="services__item">Property Law</li>
        <li class="services__item">Wills</li>
        <li class="services__item">Powers of Attorney</li>
        <li class="services__item">Probate &amp; Estate<br>Administration</li>
        <li class="services__item">Consultancy &amp; Agency</li>
      </ul>
    </section>

    <p class="tagline">We use the latest digital technology and fixed-fees to provide<br>fast and affordable legal advice that is easy to understand.</p>

    <div class="phone">
      <span class="phone__icon">
        <svg width="18" height="18" viewBox="0 0 24 24"><path fill="#fff" d="M6.6 10.8a15.1 15.1 0 0 0 6.6 6.6l2.2-2.2c.3-.3.7-.4 1-.2 1.1.4 2.3.6 3.6.6.6 0 1 .4 1 1V20c0 .6-.4 1-1 1C10.6 21 3 13.4 3 4c0-.6.4-1 1-1h3.5c.6 0 1 .4 1 1 0 1.3.2 2.5.6 3.6.1.3 0 .7-.2 1z"/></svg>
      </span>
      <span class="phone__number">555-7777-8888</span>
    </div>

    <div class="web">www.ridgeviewlawyers.com</div>
  </main>
</body>
</html>
```